Flyer für ein Jugendfestival
Zielgruppe
Wir sind ein christlicher Jugendverband, der hauptsächlich Freizeiten organisiert. Die Haupt-Zielgruppe sind somit Jugendliche im Alter von 13-17 Jahre, darüber hinaus junge Erwachsene im Alter von 18-25. Viele haben einen christlichen Kontext, viele allerdings nicht. Gemein haben alle, dass sie im Sommer unterwegs waren.
Aufgabenstellung
Der Flyer ist für das 'Open Sky Camp', unser Jugendfestival, dieses findet vom 15.-17. September 2023 statt. Motto: 'safe da.bei' Ort: Sonnwiesenau. Preis: 74€. Alter: ab 13 Jahre.
Mögliche Farbgebung in Richtung: rosa, flieder, blau oder grün (nicht allzu bunt, farblich stimmig). Inhaltlicher Schwerpunkt ist Sicherheit, muss aber nicht wörtlich vorkommen.
Es müssen keine realen Bilder vorkommen, sondern gern auch nur Silhouetten oder Farbverläufe...
Idee für die Aufteilung: Vorderseite: Daten, Rückseite: Aktionen und Teaser der Bands (Workshops, Jesus erleben, Worship, Lounge, Döner, Klangfaden-Ensemble, Morgen bleibt wach... ) Kann aber auch abweichen, da gerade noch nicht alle Acts feststehen
Somit soll der Flyer für Jugendliche ansprechend wirken, möglichst alle repräsentieren (also nicht nur eine Person, sondern mehrere oder gar keine), 'in sein' und mit dem Trend gehen.

```html
<!DOCTYPE html>
<html lang="de">
<head>
<meta charset="utf-8">
<title>Open Sky Camp – Flyer</title>
<link href="https://fonts.googleapis.com/css2?family=Bebas+Neue&family=Kaushan+Script&display=swap" rel="stylesheet">
<style>
  :root {
    --stage: #a0a0a0;
    --paper: #eef9f9;
    --plum: #7a3e6a;
    --plum-deep: #74305f;
    --brush: #9a5d88;
    --brush-light: #b285a6;
    --date-ink: #fde6f0;
    --pin: #c8102e;
    --ink: #111111;
    --list-ink: #2a1420;
    --badge: #8a4f7d;
    --accent: #f08a0c;
  }
  * { margin: 0; padding: 0; box-sizing: border-box; }
  html, body { width: 1200px; height: 1200px; overflow: hidden; background: var(--stage); }
  .stage { position: relative; width: 1200px; height: 1200px; }
  .flyer {
    position: absolute; top: 136px; width: 500px; height: 957px;
    background: var(--paper); overflow: hidden;
  }
  .flyer--front { left: 78px; }
  .flyer--back { left: 633px; }

  .art { position: absolute; }
  .front-dancers {
    left: 31px; top: 126px; width: 425px; height: 262px;
    background: radial-gradient(ellipse at 20% 60%, #f6d23c 0%, transparent 40%),
                radial-gradient(ellipse at 42% 45%, #f2683a 0%, transparent 40%),
                radial-gradient(ellipse at 62% 40%, #d63c8e 0%, transparent 40%),
                radial-gradient(ellipse at 68% 70%, #8a4fb8 0%, transparent 40%),
                radial-gradient(ellipse at 88% 55%, #2fa6c9 0%, transparent 42%);
    opacity: .85; border-radius: 40%;
  }
  .hands-row {
    left: 0; bottom: 0; width: 500px; height: 187px;
    background: linear-gradient(90deg, #f39a26, #7e7fc4, #e9383e, #46c08b, #8b3fa0, #3fb3e6, #e94f8e, #9ccc3b);
    clip-path: polygon(0 20%, 6% 8%, 12% 25%, 20% 5%, 28% 22%, 36% 0, 44% 18%, 52% 10%, 60% 26%, 68% 12%, 76% 20%, 84% 2%, 92% 15%, 100% 6%, 100% 100%, 0 100%);
  }
  .back-dancers {
    left: 0; top: 0; width: 500px; height: 464px;
    background: radial-gradient(ellipse at 15% 45%, #d9e8a8 0%, transparent 40%),
                radial-gradient(ellipse at 45% 35%, #f2c6d6 0%, transparent 40%),
                radial-gradient(ellipse at 65% 40%, #dcc7e6 0%, transparent 42%),
                radial-gradient(ellipse at 88% 50%, #bfe2ee 0%, transparent 42%);
    opacity: .8;
  }

  .event-title {
    position: absolute; left: 0; width: 500px; top: 66px; text-align: center;
    font: 400 54px/1 "Kaushan Script", cursive; color: var(--plum); transform: rotate(-4deg);
  }
  .age-badge {
    position: absolute; left: 44px; top: 315px; width: 106px; height: 106px; border-radius: 50%;
    background: var(--badge); color: #fff; text-align: center;
    font-family: "Kaushan Script", cursive;
  }
  .age-badge .age { display: block; font-size: 38px; line-height: 1; margin-top: 16px; }
  .age-badge .unit { display: block; font-size: 22px; line-height: 1; margin-top: 4px; transform: rotate(-8deg); }

  .intro {
    position: absolute; left: 0; width: 500px; top: 447px; text-align: center;
    font: 400 20px/1 Arial, Helvetica, sans-serif; color: var(--ink); transform: rotate(-3deg);
  }
  .brush-band { position: absolute; }
  .brush-band--date { left: 6px; top: 488px; width: 491px; height: 125px; }
  .brush-band--heading { left: 25px; top: 280px; width: 460px; height: 110px; }

  .event-date {
    position: absolute; left: 0; width: 500px; top: 508px; text-align: center;
    font: 400 58px/1 "Bebas Neue", sans-serif; color: var(--date-ink); transform: rotate(-3deg);
  }
  .venue {
    position: absolute; left: 112px; top: 590px; display: flex; align-items: center; gap: 6px;
    font: 400 42px/1 "Bebas Neue", sans-serif; color: var(--plum-deep);
  }
  .price {
    position: absolute; left: 0; width: 500px; top: 700px; text-align: center;
    font: 400 40px/1 "Kaushan Script", cursive; color: var(--ink);
  }

  .brand {
    position: absolute; left: 98px; top: 92px; display: flex; align-items: center; gap: 12px;
  }
  .brand-name { font: 400 86px/1 "Bebas Neue", sans-serif; color: #1b1b1b; letter-spacing: 2px; }
  .brand-dot { width: 36px; height: 36px; border-radius: 50%; background: var(--accent); }

  .section-heading {
    position: absolute; left: 0; width: 500px; top: 312px; text-align: center;
    font: 400 36px/1 "Bebas Neue", sans-serif; color: #fff; transform: rotate(-4deg);
  }
  .program { position: absolute; left: 0; width: 506px; top: 418px; list-style: none; text-align: center; }
  .program li { font: 400 26px/1 Arial, Helvetica, sans-serif; color: var(--list-ink); height: 49px; }
</style>
</head>
<body>
<div class="stage">

  <section class="flyer flyer--front">
    <div class="art front-dancers" role="img" aria-label="Aquarell-Silhouetten springender Jugendlicher in Gelb, Orange, Pink, Lila und Blau"></div>
    <h1 class="event-title">Open Sky Camp</h1>
    <div class="age-badge"><span class="age">+13</span><span class="unit">Jahre</span></div>
    <p class="intro">Unser Jugendfestival, dieses findet vom</p>
    <svg class="brush-band brush-band--date" viewBox="0 0 491 125" aria-hidden="true">
      <polygon points="18,30 470,12 488,22 462,70 480,80 455,92 60,118 40,108 70,100 8,88 30,70 0,62" fill="var(--brush)"/>
      <polygon points="120,5 420,0 410,6 130,10" fill="var(--brush-light)"/>
      <polygon points="60,112 360,100 350,106 70,120" fill="var(--brush-light)"/>
    </svg>
    <p class="event-date">15-17 September 2023</p>
    <div class="venue">
      <svg width="36" height="54" viewBox="0 0 36 54" aria-hidden="true">
        <path d="M18 0C8 0 0 8 0 18c0 13 18 36 18 36s18-23 18-36C36 8 28 0 18 0z" fill="var(--pin)"/>
        <circle cx="18" cy="17" r="7" fill="#fff"/>
      </svg>
      <span>Sonnwiesenau</span>
    </div>
    <p class="price">Preis: 74€</p>
    <div class="art hands-row" role="img" aria-label="Bunte erhobene Hände im Low-Poly-Stil"></div>
  </section>

  <section class="flyer flyer--back">
    <div class="art back-dancers" role="img" aria-label="Blasse Aquarell-Silhouetten springender Jugendlicher"></div>
    <div class="brand"><span class="brand-name">Weitblick</span><span class="brand-dot"></span></div>
    <svg class="brush-band brush-band--heading" viewBox="0 0 460 110" aria-hidden="true">
      <polygon points="20,50 455,15 448,30 420,62 440,70 60,100 30,95 45,86 0,80 15,65" fill="var(--brush)"/>
      <polygon points="190,12 420,0 415,6 200,16" fill="var(--brush-light)"/>
    </svg>
    <h2 class="section-heading">Aktionen und Teaser der Bands</h2>
    <ul class="program">
      <li>Workshops</li>
      <li>Jesus erleben</li>
      <li>Worship</li>
      <li>Lounge</li>
      <li>Klangfaden–Ensemble</li>
      <li>Döner</li>
      <li>Morgen bleibt wach</li>
    </ul>
    <div class="art hands-row" role="img" aria-label="Bunte erhobene Hände im Low-Poly-Stil"></div>
  </section>

</div>
</body>
</html>
```